Stationery for Software Developer
Glen Ambrose
Project: Stationery for Software Developer
Stationery for Software Developer - Information Technology
Creative Brief
Professional
Software Engineer
Greater Harbor Valley
glen@ambrosk.me
http://ambrosk.me
Chirpline: @ambrog Circlr+: +GlenAmbrose Facepage: gambrosk WorkNexus: glenambrose (Prefer Social Icons to be used instead of the names)
Main Logo with name on front. Open to variations of the main logo on front.
sevensky sevensky
gambrosk gambrosk
My apologies. I accidentally started this project before I had my logo in hand. I have contacted support about suspending this contest for 4 days until I have it. Thanks for the interest! Glen
paul1990 paul1990
Hi, Where is your logo?

```html
<!DOCTYPE html>
<html lang="en">
<head>
<meta charset="utf-8">
<title>Glen Ambrose — Business Card</title>
<link href="https://fonts.googleapis.com/css2?family=Open+Sans:wght@300;400&display=swap" rel="stylesheet">
<style>
  :root {
    --backdrop: #e9e4dc;
    --paper: #ffffff;
    --navy: #3f4b66;
    --ink-light: #eef1f6;
    --ink-muted: #b9c2d3;
    --ink-front: #4a5570;
    --teal: #6fc7c4;
    --pink: #d36aa8;
    --violet: #8a6fae;
    --rule: #c9ced8;
  }
  * { box-sizing: border-box; margin: 0; padding: 0; }
  html, body {
    width: 1200px; height: 881px; overflow: hidden;
    background: var(--backdrop);
    font-family: "Open Sans", Arial, sans-serif;
  }
  .sheet {
    width: 1200px; height: 881px;
    display: flex; align-items: center; justify-content: center; gap: 60px;
  }
  .card {
    width: 520px; height: 297px; border-radius: 4px;
    box-shadow: 0 6px 18px rgba(0,0,0,.12);
    position: relative;
  }
  /* front */
  .card--front {
    background: var(--paper);
    display: flex; align-items: center; justify-content: center; gap: 22px;
  }
  .brand-mark { width: 46px; height: 46px; background: var(--teal); flex: none; }
  .brand-divider { width: 1px; height: 70px; background: var(--rule); }
  .brand-name {
    font-weight: 300; font-size: 38px; color: var(--ink-front); letter-spacing: .5px;
    white-space: nowrap;
  }
  /* back */
  .card--back { background: var(--navy); color: var(--ink-light); padding: 30px 34px; }
  .person-name { font-weight: 300; font-size: 22px; }
  .person-title { font-weight: 300; font-size: 12px; color: var(--ink-muted); margin-top: 2px; }
  .contact-list { list-style: none; margin-top: 22px; }
  .contact-list li {
    display: flex; align-items: center; gap: 10px;
    font-size: 11.5px; font-weight: 300; line-height: 20px; white-space: nowrap;
  }
  .contact-icon { width: 12px; height: 12px; flex: none; }
  .social-square { width: 12px; height: 12px; flex: none; }
  .social-square--teal { background: var(--teal); }
  .social-square--pink { background: var(--pink); }
  .social-square--violet { background: var(--violet); }
  .social-label { color: var(--ink-muted); }
  .back-brand {
    position: absolute; right: 40px; top: 50%; transform: translateY(-50%);
    display: flex; flex-direction: column; align-items: center; gap: 12px;
  }
  .back-brand .brand-mark { width: 90px; height: 90px; border-radius: 50%; background: var(--teal); }
  .back-brand .brand-name { font-size: 16px; color: var(--ink-light); }
</style>
</head>
<body>
<main class="sheet">
  <section class="card card--front">
    <div class="brand-mark"></div>
    <div class="brand-divider"></div>
    <h1 class="brand-name">Glen Ambrose</h1>
  </section>

  <section class="card card--back">
    <h2 class="person-name">Glen Ambrose</h2>
    <p class="person-title">Software Engineer</p>
    <ul class="contact-list">
      <li>
        <svg class="contact-icon" viewBox="0 0 12 12"><path d="M6 0.5a4 4 0 0 0-4 4c0 3 4 7 4 7s4-4 4-7a4 4 0 0 0-4-4z" fill="var(--ink-light)"/><circle cx="6" cy="4.5" r="1.4" fill="var(--navy)"/></svg>
        Greater Harbor Valley
      </li>
      <li>
        <svg class="contact-icon" viewBox="0 0 12 12"><rect x="3" y="0.5" width="6" height="11" rx="1.2" fill="var(--ink-light)"/><rect x="4" y="2" width="4" height="7" fill="var(--navy)"/></svg>
        +1 555 014 2290
      </li>
      <li>
        <svg class="contact-icon" viewBox="0 0 12 12"><rect x="0.5" y="2.5" width="11" height="7" fill="var(--ink-light)"/><path d="M0.5 2.5l5.5 4 5.5-4" stroke="var(--navy)" fill="none"/></svg>
        glen@ambrosk.me
      </li>
      <li>
        <svg class="contact-icon" viewBox="0 0 12 12"><circle cx="6" cy="6" r="5" stroke="var(--ink-light)" fill="none"/><path d="M1 6h10M6 1c2 2 2 8 0 10M6 1c-2 2-2 8 0 10" stroke="var(--ink-light)" fill="none"/></svg>
        http://ambrosk.me
      </li>
      <li><span class="social-square social-square--teal"></span><span class="social-label">Chirpline</span> @ambrog</li>
      <li><span class="social-square social-square--pink"></span><span class="social-label">Circlr+</span> +GlenAmbrose</li>
      <li><span class="social-square social-square--violet"></span><span class="social-label">Facepage</span> gambrosk</li>
      <li><span class="social-square social-square--teal"></span><span class="social-label">WorkNexus</span> glenambrose</li>
    </ul>
    <div class="back-brand">
      <div class="brand-mark"></div>
      <span class="brand-name">Glen Ambrose</span>
    </div>
  </section>
</main>
</body>
</html>
```